Spiritual Healer needs design for Wordpress

I am a spiritual healer and I need a Wordpress design to offer my distant healing services on a website. It's like Reiki but I use my own healing modality.
It would be great to have a magical design with beautiful colors like purple, I will upload some images so you get an idea of the feel.
The design should communicate lightness and peacefulness, I like playfulness in the design not too blocky.
Need a complete website design, including navigation bar. I do not have a logo yet.

Target Market(s)

Everyone

Requirements
Nice to have
• Works on mobile devices
Should not have
• Too much of typical spiritual symbols on it.

```html
<!DOCTYPE html>
<html lang="en">
<head>
<meta charset="utf-8">
<title>Spiritual Healing</title>
<link rel="stylesheet" href="https://fonts.googleapis.com/css2?family=Arimo:wght@400&family=PT+Sans:wght@400&family=Dancing+Script:wght@700&family=Fjalla+One&family=Patrick+Hand&display=swap">
<style>
:root{
  --purple-deep:#2a0640;
  --purple:#6a0d97;
  --purple-mid:#5a0c85;
  --lavender:#b97be8;
  --script:#c67cf0;
  --black:#050308;
  --white:#ffffff;
  --ink:#111111;
  --sky-top:#9f8fd0;
  --sky-mid:#c3a6cf;
  --hill:#4a3a52;
  --lake:#2d2f5a;
}
*{margin:0;padding:0;box-sizing:border-box}
html,body{width:853px;height:1200px;overflow:hidden}
body{position:relative;font-family:'Arimo',Arial,sans-serif;color:var(--white);background:var(--lake)}
.scenery{position:absolute;left:0;top:147px;width:853px;height:943px;
  background:linear-gradient(180deg,var(--sky-top) 0%,var(--sky-mid) 18%,#8f7896 30%,var(--hill) 44%,#5d4f7a 56%,var(--lake) 68%,#47406a 80%,#3b2f4a 100%)}
.top-band{position:absolute;left:0;top:0;width:853px;height:147px;
  background:linear-gradient(180deg,var(--purple-deep) 0%,var(--purple) 100%)}
.nav-top{position:absolute;top:26px;list-style:none;font-family:'PT Sans',sans-serif;font-size:15.5px;line-height:31px}
.nav-top a{color:var(--white);text-decoration:none}
.nav-left{right:650px;text-align:right}
.nav-right{left:637px}
.feature{position:absolute;left:262px;top:0;width:328px;height:682px;background:var(--black)}
.brand{position:absolute;left:0;top:8px;width:328px;text-align:center;font-weight:400}
.brand-script{display:block;font-family:'Dancing Script',cursive;font-size:48px;line-height:50px;color:var(--script);margin-left:-10px}
.brand-main{display:block;font-family:'Fjalla One',sans-serif;font-size:82px;line-height:90px;color:var(--white);letter-spacing:0}
.feature-glow{position:absolute;left:0;top:150px;width:328px;height:340px;
  background:radial-gradient(ellipse 110px 50px at 50% 22%,#f3c8f4 0%,#b45cc4 40%,transparent 100%),
  linear-gradient(180deg,#201632 0%,#3a2147 35%,#1a1020 70%,var(--black) 100%)}
.feature-photo{position:absolute;left:16px;top:493px;width:297px;height:175px;border-radius:18px;
  background:linear-gradient(135deg,#7fa04a 0%,#c4557e 45%,#e08bb0 60%,#5b7d3d 100%)}
.section-title{position:absolute;font-family:'Patrick Hand',cursive;font-weight:400;font-size:28px;line-height:30px;color:var(--ink);text-align:center;letter-spacing:1px;text-transform:uppercase;white-space:nowrap}
.copy{position:absolute;font-size:15px;line-height:17.2px;text-align:justify;overflow:hidden}
.intro-copy{left:89px;top:741px;width:684px;font-size:17px;line-height:19px;overflow:visible}
.cards{position:absolute;left:24px;top:867px;display:flex;gap:7px}
.card{width:195px}
.card-photo{height:130px;border:3px solid var(--lavender);border-radius:4px}
.card-text{font-size:12px;line-height:17px;text-align:justify;padding:4px 4px 0}
.footer{position:absolute;left:0;top:1090px;width:853px;height:110px;
  background:linear-gradient(180deg,var(--purple-mid) 0%,#1a0526 100%)}
.nav-bottom{position:absolute;top:14px;width:100%;text-align:center;font-family:'Arimo',sans-serif;font-size:16px}
.nav-bottom a{color:var(--white);text-decoration:none}
.nav-bottom .sep{margin:0 11px}
.social{position:absolute;top:49px;width:100%;display:flex;justify-content:center;gap:14px;list-style:none;font-size:11px;line-height:28px}
.social li{display:flex;align-items:center;gap:4px}
.social .dot{width:28px;height:28px;border-radius:50%;background:var(--lavender)}
</style>
</head>
<body>
<div class="scenery" role="img" aria-label="Landscape of mountains above a calm lake at dusk"></div>
<header class="top-band">
  <ul class="nav-top nav-left">
    <li><a href="#">HOME &gt;&gt;</a></li>
    <li><a href="#">ABOUT ME &gt;&gt;</a></li>
    <li><a href="#">COMMUNITY &gt;&gt;</a></li>
  </ul>
  <ul class="nav-top nav-right">
    <li><a href="#">&lt;&lt; MY MISSION</a></li>
    <li><a href="#">&lt;&lt; HEALING PRAYERS</a></li>
    <li><a href="#">&lt;&lt; CONTACT</a></li>
  </ul>
</header>
<section class="feature">
  <div class="feature-glow" role="img" aria-label="Open hand radiating soft purple light downward"></div>
  <h1 class="brand"><span class="brand-script">Spiritual</span><span class="brand-main">HEALING</span></h1>
  <div class="feature-photo" role="img" aria-label="Group of people in colourful clothes raising their hands in prayer outdoors"></div>
</section>

<h2 class="section-title" style="left:35px;top:205px;width:199px">Welcome</h2>
<p class="copy" style="left:40px;top:253px;width:199px;height:240px">Lorem ipsum dolor sit amet, consectetur adipisicing elit, sed do eiusmod tempor incididunt ut labore et dolore magna aliqua. Ut enim ad minim veniam, quis nostrud exercitation ullamco laboris nisi ut aliquip ex ea commodo consequat. Duis aute irure dolor in reprehenderit in voluptate velit esse cillum dolore eu fugiat nulla pariatur. Excepteur sint occaecat cupidatat non proident.</p>

<h2 class="section-title" style="left:33px;top:515px;width:199px">Testimonials</h2>
<p class="copy" style="left:40px;top:548px;width:199px">Lorem ipsum dolor sit amet, consectetur adipisicing elit, sed do eiusmod tempor incididunt ut labore et dolore magna aliqua. Ut enim ad minim veniam, quis nostrud exercitation ullamco laboris nisi ut aliquip ex ea commodo consequat.</p>

<h2 class="section-title" style="left:603px;top:206px;width:220px">Healing Schedule</h2>
<p class="copy" style="left:621px;top:253px;width:201px;height:240px">Lorem ipsum dolor sit amet, consectetur adipisicing elit, sed do eiusmod tempor incididunt ut labore et dolore magna aliqua. Ut enim ad minim veniam, quis nostrud exercitation ullamco laboris nisi ut aliquip ex ea commodo consequat. Duis aute irure dolor in reprehenderit in voluptate velit esse cillum dolore eu fugiat nulla pariatur. Excepteur sint occaecat cupidatat non proident.</p>

<h2 class="section-title" style="left:600px;top:515px;width:220px">Healing Prayers</h2>
<p class="copy" style="left:617px;top:548px;width:201px">Lorem ipsum dolor sit amet, consectetur adipisicing elit, sed do eiusmod tempor incididunt ut labore et dolore magna aliqua. Ut enim ad minim veniam, quis nostrud exercitation ullamco laboris nisi ut aliquip ex ea commodo consequat.</p>

<h2 class="section-title" style="left:326px;top:697px;width:200px">Introduction</h2>
<p class="copy intro-copy">Lorem ipsum dolor sit amet, consectetur adipisicing elit, sed do eiusmod tempor incididunt ut labore et dolore magna aliqua. Ut enim ad minim veniam, quis nostrud exercitation ullamco laboris nisi ut aliquip ex ea commodo consequat. Duis aute irure dolor in reprehenderit in voluptate velit esse cillum dolore eu fugiat nulla pariatur. Excepteur sint occaecat cupidatat non proident, sunt in culpa qui officia deserunt mollit anim id est laborum.</p>

<div class="cards">
  <article class="card">
    <div class="card-photo" role="img" aria-label="Healer holding out his hands in a bright room" style="background:linear-gradient(135deg,#e8e8e4,#8a8a86 60%,#3a3030)"></div>
    <p class="card-text">Lorem ipsum dolor sit amet, consectetur adipisicing elit, sed do eiusmod tempor incididunt ut labore et dolore magna aliqua.</p>
  </article>
  <article class="card">
    <div class="card-photo" role="img" aria-label="Smiling man showing both open palms against a violet backdrop" style="background:linear-gradient(135deg,#b56ae6,#d9a886 50%,#8a3fcf)"></div>
    <p class="card-text">Lorem ipsum dolor sit amet, consectetur adipisicing elit, sed do eiusmod tempor incididunt ut labore et dolore magna aliqua.</p>
  </article>
  <article class="card">
    <div class="card-photo" role="img" aria-label="Preacher in white robe blessing from a pulpit" style="background:linear-gradient(160deg,#050505 40%,#d9d6d0 65%,#8a1c2a)"></div>
    <p class="card-text">Lorem ipsum dolor sit amet, consectetur adipisicing elit, sed do eiusmod tempor incididunt ut labore et dolore magna aliqua.</p>
  </article>
  <article class="card">
    <div class="card-photo" role="img" aria-label="Hands resting gently on a person's head" style="background:linear-gradient(135deg,#c89a86,#6a4a3a 60%,#2a1a14)"></div>
    <p class="card-text">Lorem ipsum dolor sit amet, consectetur adipisicing elit, sed do eiusmod tempor incididunt ut labore et dolore magna aliqua.</p>
  </article>
</div>

<footer class="footer">
  <nav class="nav-bottom">
    <a href="#">HOME</a><span class="sep">|</span><a href="#">ABOUT ME</a><span class="sep">|</span><a href="#">COMMUNITY</a><span class="sep">|</span><a href="#">MY MISSION</a><span class="sep">|</span><a href="#">HEALING PRAYERS</a><span class="sep">|</span><a href="#">CONTACT</a>
  </nav>
  <ul class="social">
    <li><span class="dot"></span>Circlet</li>
    <li><span class="dot"></span>Chirpa</li>
    <li><span class="dot"></span>Plusora</li>
    <li><span class="dot"></span>Pinvale</li>
    <li><span class="dot"></span>Newsline</li>
  </ul>
</footer>
</body>
</html>
```